Design a leading edge business card for an architectural company

We believe that Velistra Design Collective is redefining the architectural industry. With that, we need a leading edge business card for the company that focuses on landscape architecture, design, and construction.

Our clients are businesses and homeowners so we need a clean, simple, and professional-looking logo. But we want something special. Design must be elegant but unexpected.

Color preferences:
- Preferably with black background but not a must
- Text should be light colored
- Overall, don’t use too much colors.

Content:
- Front of card must contain either just the logo or the logo and business name only.
- Back of card will show the other information (name, title, phone number, email, website, location).

Style:
- Maybe embossing, de-bossing, or spot UV
- Layout should be landscape unless you prove us otherwise.

Size: 1050 x 600 pixels (with 1/8th inch bleed: 1125 x 675 pixels)

Attached is the company logo to incorporate in the design.

```html
<!DOCTYPE html>
<html lang="en">
<head>
<meta charset="utf-8">
<title>Velistra Design Collective — Business Cards</title>
<link rel="stylesheet" href="https://fonts.googleapis.com/css2?family=Open+Sans:wght@300;400&display=swap">
<style>
  :root {
    --backdrop: #e4e1dd;
    --card-black: #0b0b0c;
    --card-sheen: #1c1c1f;
    --ink-light: #f2f2f2;
    --ink-muted: #c9c9cc;
    --icon-fill: #ffffff;
    --icon-glyph: #0b0b0c;
  }
  * { margin: 0; padding: 0; box-sizing: border-box; }
  html, body {
    width: 1200px;
    height: 912px;
    overflow: hidden;
    background: var(--backdrop);
    font-family: "Open Sans", Arial, sans-serif;
  }
  .canvas {
    position: relative;
    width: 1200px;
    height: 912px;
    display: flex;
    justify-content: center;
    align-items: center;
    gap: 100px;
  }
  .card {
    position: relative;
    width: 380px;
    height: 640px;
    background:
      linear-gradient(115deg, transparent 38%, rgba(255,255,255,0.06) 46%, transparent 56%),
      linear-gradient(160deg, var(--card-sheen) 0%, var(--card-black) 55%);
    border-radius: 4px;
    box-shadow: 0 18px 40px rgba(0,0,0,0.28);
    color: var(--ink-light);
    text-align: center;
  }
  .brand {
    position: absolute;
    top: 92px;
    left: 0;
    right: 0;
    display: flex;
    flex-direction: column;
    align-items: center;
    gap: 16px;
  }
  .brand-mark {
    width: 34px;
    height: 34px;
    border: 2px solid var(--ink-light);
    border-radius: 50%;
  }
  .brand-name {
    font-weight: 300;
    font-size: 22px;
    letter-spacing: 0.22em;
    line-height: 1.45;
    text-transform: uppercase;
    color: var(--ink-light);
    width: 300px;
  }
  .person {
    position: absolute;
    top: 270px;
    left: 0;
    right: 0;
  }
  .person-name {
    font-weight: 400;
    font-size: 22px;
    letter-spacing: 0.02em;
  }
  .person-title {
    font-weight: 300;
    font-size: 13px;
    color: var(--ink-muted);
    margin-top: 2px;
  }
  .contact-list {
    position: absolute;
    top: 352px;
    left: 0;
    right: 0;
    list-style: none;
    display: flex;
    flex-direction: column;
    align-items: center;
    gap: 10px;
  }
  .contact-item {
    display: flex;
    flex-direction: column;
    align-items: center;
    gap: 6px;
    font-weight: 300;
    font-size: 14px;
    color: var(--ink-light);
  }
  .contact-icon {
    width: 22px;
    height: 22px;
    background: var(--icon-fill);
    border-radius: 3px;
    display: flex;
    align-items: center;
    justify-content: center;
  }
  .contact-icon svg { width: 14px; height: 14px; }
  .card-front .brand { top: 210px; }
  .front-web {
    position: absolute;
    bottom: 70px;
    left: 0;
    right: 0;
    font-weight: 300;
    font-size: 14px;
    color: var(--ink-light);
  }
</style>
</head>
<body>
<main class="canvas">

  <section class="card card-back" aria-label="Card back with contact details">
    <div class="brand">
      <span class="brand-mark" aria-hidden="true"></span>
      <span class="brand-name">Velistra Design Collective</span>
    </div>

    <div class="person">
      <p class="person-name">Arlen Voss</p>
      <p class="person-title">Marketing Manager</p>
    </div>

    <ul class="contact-list">
      <li class="contact-item">
        <span class="contact-icon">
          <svg viewBox="0 0 24 24" aria-hidden="true"><path fill="var(--icon-glyph)" d="M6.6 2.5 9.4 6c.4.5.4 1.2 0 1.7L7.9 9.4a13 13 0 0 0 6.7 6.7l1.7-1.5c.5-.4 1.2-.4 1.7 0l3.5 2.8c.5.4.6 1.2.1 1.7l-1.8 2c-.6.6-1.5.9-2.4.7C9.9 20.2 3.8 14.1 2.2 6.6c-.2-.9.1-1.8.7-2.4l2-1.8c.5-.4 1.3-.4 1.7.1z"/></svg>
        </span>
        <span>312 555 0148</span>
      </li>
      <li class="contact-item">
        <span class="contact-icon">
          <svg viewBox="0 0 24 24" aria-hidden="true" fill="none" stroke="var(--icon-glyph)" stroke-width="2"><circle cx="12" cy="12" r="9"/><ellipse cx="12" cy="12" rx="4" ry="9"/><path d="M3 12h18"/></svg>
        </span>
        <span>www.velistracollective.com</span>
      </li>
      <li class="contact-item">
        <span class="contact-icon">
          <svg viewBox="0 0 24 24" aria-hidden="true"><path fill="var(--icon-glyph)" d="M12 3 2 12h3v8h5v-5h4v5h5v-8h3z"/></svg>
        </span>
        <span>Address line1, Address line2</span>
      </li>
      <li class="contact-item">
        <span class="contact-icon">
          <svg viewBox="0 0 24 24" aria-hidden="true" fill="none" stroke="var(--icon-glyph)" stroke-width="2.2"><circle cx="12" cy="12" r="3.5"/><path d="M15.5 12v1.5a2.5 2.5 0 0 0 5 0V12a8.5 8.5 0 1 0-3.5 6.9"/></svg>
        </span>
        <span>arlen@velistracollective.com</span>
      </li>
    </ul>
  </section>

  <section class="card card-front" aria-label="Card front with company name">
    <div class="brand">
      <span class="brand-mark" aria-hidden="true"></span>
      <span class="brand-name">Velistra Design Collective</span>
    </div>
    <p class="front-web">www.velistracollective.com</p>
  </section>

</main>
</body>
</html>
```